Design Android App for Creating Estimates and Invoices

This project is to create a graphic design for an Android mobile app called Velmira Contractor App which is an app that will help contractors to quickly create professional estimates and invoices, accept payments, manage clients and projects and run their business smoothly.

Link to some designs I created myself, hoping to get even better design from you
https://pixtray.example/album/qRwoPe

This project is similar to
https://apps.storefrontia.example/details?id=com.bracklyapp.android.brackly
https://apps.storefrontia.example/details?id=com.zeltru.billnote

Check this Google Doc for more information. http://shrtn.example/8KqPmX1

Target Market(s)

Contractors, Home Improvement Professionals, Home Builders,

Industry/Entity Type

Residential Construction

Requirements
Must have
• Non-cluttered screen for Estimates, Enough white space between fields.
Nice to have
• Be different from the two example designs shown

```html
<!DOCTYPE html>
<html lang="en">
<head>
<meta charset="UTF-8">
<title>Velmira Contractor App – Invoices</title>
<link href="https://fonts.googleapis.com/css2?family=Roboto:wght@400;500&display=swap" rel="stylesheet">
<style>
  :root {
    --page-bg: #dde3f6;
    --status-blue: #2f5196;
    --bar-blue: #3558a0;
    --tab-muted: #a9bbe3;
    --white: #ffffff;
    --list-bg: #f2f3f8;
    --text-dark: #3a3d45;
    --text-muted: #7d808a;
    --amount-orange: #f26b10;
    --total-green: #7cc21b;
    --accent-green: #86c82a;
    --accent-orange: #f47a20;
    --nav-grey: #8f96aa;
    --avatar-tone: #b48e76;
  }
  * { box-sizing: border-box; margin: 0; padding: 0; }
  html, body { width: 1200px; height: 1200px; overflow: hidden; }
  body {
    background: var(--page-bg);
    font-family: "Roboto", sans-serif;
    position: relative;
  }
  .screen {
    position: absolute; left: 283px; top: 35px;
    width: 634px; height: 1130px;
    background: var(--list-bg);
    overflow: hidden;
    box-shadow: 0 10px 40px rgba(40, 60, 120, 0.18);
  }
  .status-bar {
    position: absolute; left: 0; top: 0; width: 100%; height: 42px;
    background: var(--status-blue);
    display: flex; align-items: center; justify-content: flex-end;
    gap: 10px; padding-right: 14px; color: var(--white);
    font-size: 23px;
  }
  .app-bar {
    position: absolute; left: 0; top: 42px; width: 100%; height: 192px;
    background: var(--bar-blue); color: var(--white);
  }
  .menu-icon { position: absolute; left: 24px; top: 56px; }
  .app-title { position: absolute; left: 89px; top: 47px; font-size: 31px; font-weight: 400; }
  .search-icon { position: absolute; left: 530px; top: 53px; }
  .more-icon { position: absolute; left: 590px; top: 53px; }
  .tabs { position: absolute; left: 0; bottom: 0; width: 100%; height: 60px; display: flex; }
  .tab {
    flex: 1; text-align: center; font-size: 18px; line-height: 52px;
    color: var(--tab-muted); letter-spacing: 0.3px; position: relative;
  }
  .tab.is-active { color: var(--white); }
  .tab.is-active::after {
    content: ""; position: absolute; left: 0; right: 0; bottom: 0; height: 4px;
    background: var(--white);
  }
  .filter-row {
    position: absolute; left: 0; top: 234px; width: 100%; height: 58px;
    background: var(--white);
    display: flex; align-items: center; justify-content: space-between;
    padding: 0 24px;
  }
  .year-select { font-size: 19px; color: var(--text-dark); display: flex; align-items: center; gap: 14px; }
  .total { font-size: 19px; color: var(--total-green); font-weight: 500; }
  .invoice-list { position: absolute; left: 24px; top: 309px; width: 584px; }
  .invoice-card {
    position: relative; height: 119px; margin-bottom: 15px;
    background: var(--white); border-radius: 3px;
    box-shadow: 0 1px 3px rgba(0, 0, 0, 0.08);
  }
  .avatar {
    position: absolute; left: 19px; top: 26px; width: 66px; height: 66px;
    border-radius: 50%;
    background: radial-gradient(circle at 50% 40%, #d3ad92, var(--avatar-tone) 60%, #5c4f48);
  }
  .client-name {
    position: absolute; left: 110px; top: 31px; font-size: 19px; font-weight: 500;
    color: var(--text-dark); display: flex; align-items: center; gap: 10px;
  }
  .badge { width: 24px; height: 24px; border-radius: 50%; display: inline-flex; align-items: center; justify-content: center; }
  .badge.phone { background: var(--accent-green); margin-left: 4px; }
  .badge.mail { background: var(--accent-orange); }
  .invoice-number { position: absolute; left: 110px; top: 71px; font-size: 15px; color: var(--text-muted); }
  .amount { position: absolute; right: 18px; top: 31px; font-size: 18px; font-weight: 500; color: var(--amount-orange); }
  .due-date { position: absolute; right: 18px; top: 73px; font-size: 13px; color: var(--text-muted); }
  .fab {
    position: absolute; left: 548px; top: 945px; width: 60px; height: 60px; border-radius: 50%;
    background: var(--accent-green); display: flex; align-items: center; justify-content: center;
    box-shadow: 0 4px 10px rgba(0, 0, 0, 0.2);
  }
  .bottom-nav {
    position: absolute; left: 0; top: 1040px; width: 100%; height: 90px;
    background: var(--white); display: flex;
  }
  .nav-item {
    flex: 1; display: flex; flex-direction: column; align-items: center;
    padding-top: 12px; gap: 10px; font-size: 14px; letter-spacing: 0.4px; color: var(--nav-grey);
  }
  .nav-item.is-active { color: var(--accent-orange); font-weight: 500; }
  .nav-item.is-dim { color: #b4b9c8; }
</style>
</head>
<body>
<main class="screen">
  <div class="status-bar">
    <svg width="30" height="24" viewBox="0 0 30 24"><path d="M1 6 Q15 -4 29 6 L15 23 Z" fill="#fff"/></svg>
    <svg width="24" height="24" viewBox="0 0 24 24"><path d="M23 1 V23 H1 Z" fill="#fff"/></svg>
    <svg width="14" height="24" viewBox="0 0 14 24"><rect x="0" y="2" width="14" height="22" rx="1" fill="#fff"/><rect x="4" y="0" width="6" height="3" fill="#fff"/></svg>
    <span>12:30</span>
  </div>

  <header class="app-bar">
    <svg class="menu-icon" width="33" height="22" viewBox="0 0 33 22"><g fill="#fff"><rect y="0" width="33" height="3"/><rect y="9.5" width="33" height="3"/><rect y="19" width="33" height="3"/></g></svg>
    <h1 class="app-title">Invoices</h1>
    <svg class="search-icon" width="30" height="30" viewBox="0 0 30 30"><circle cx="12.5" cy="12.5" r="10" fill="none" stroke="#fff" stroke-width="2.5"/><line x1="20" y1="20" x2="28" y2="28" stroke="#fff" stroke-width="2.5" stroke-linecap="round"/></svg>
    <svg class="more-icon" width="10" height="30" viewBox="0 0 10 30"><g fill="#fff"><circle cx="5" cy="4" r="3.2"/><circle cx="5" cy="15" r="3.2"/><circle cx="5" cy="26" r="3.2"/></g></svg>
    <nav class="tabs">
      <div class="tab">ALL</div>
      <div class="tab is-active">OUTSTANDING</div>
      <div class="tab">PAID</div>
    </nav>
  </header>

  <div class="filter-row">
    <div class="year-select">2017
      <svg width="12" height="8" viewBox="0 0 12 8"><path d="M1 1 L6 6 L11 1" fill="none" stroke="#3a3d45" stroke-width="1.8"/></svg>
    </div>
    <div class="total">$7891.25</div>
  </div>

  <section class="invoice-list">
    <article class="invoice-card">
      <div class="avatar" role="img" aria-label="Client portrait photo"></div>
      <div class="client-name">Eadric Gill
        <span class="badge phone"><svg width="12" height="12" viewBox="0 0 12 12"><path d="M2 1 L4.5 1 L5.5 3.5 L4 4.6 Q5 7 7.4 8 L8.5 6.5 L11 7.5 L11 10 Q6 11 3 8 Q0.5 5 2 1 Z" fill="#fff"/></svg></span>
        <span class="badge mail"><svg width="13" height="10" viewBox="0 0 13 10"><rect x="0.5" y="0.5" width="12" height="9" rx="1" fill="#fff"/><path d="M1 1 L6.5 5.5 L12 1" fill="none" stroke="#f47a20" stroke-width="1.3"/></svg></span>
      </div>
      <div class="invoice-number">INV0001</div>
      <div class="amount">$1,234.56</div>
      <div class="due-date">Due 11/06/2017</div>
    </article>
    <article class="invoice-card">
      <div class="avatar" role="img" aria-label="Client portrait photo"></div>
      <div class="client-name">Fang Collins
        <span class="badge phone"><svg width="12" height="12" viewBox="0 0 12 12"><path d="M2 1 L4.5 1 L5.5 3.5 L4 4.6 Q5 7 7.4 8 L8.5 6.5 L11 7.5 L11 10 Q6 11 3 8 Q0.5 5 2 1 Z" fill="#fff"/></svg></span>
        <span class="badge mail"><svg width="13" height="10" viewBox="0 0 13 10"><rect x="0.5" y="0.5" width="12" height="9" rx="1" fill="#fff"/><path d="M1 1 L6.5 5.5 L12 1" fill="none" stroke="#f47a20" stroke-width="1.3"/></svg></span>
      </div>
      <div class="invoice-number">INV0002</div>
      <div class="amount">$1,234.56</div>
      <div class="due-date">Due 11/06/2017</div>
    </article>
    <article class="invoice-card">
      <div class="avatar" role="img" aria-label="Client portrait photo"></div>
      <div class="client-name">Jack Watson
        <span class="badge phone"><svg width="12" height="12" viewBox="0 0 12 12"><path d="M2 1 L4.5 1 L5.5 3.5 L4 4.6 Q5 7 7.4 8 L8.5 6.5 L11 7.5 L11 10 Q6 11 3 8 Q0.5 5 2 1 Z" fill="#fff"/></svg></span>
        <span class="badge mail"><svg width="13" height="10" viewBox="0 0 13 10"><rect x="0.5" y="0.5" width="12" height="9" rx="1" fill="#fff"/><path d="M1 1 L6.5 5.5 L12 1" fill="none" stroke="#f47a20" stroke-width="1.3"/></svg></span>
      </div>
      <div class="invoice-number">INV0003</div>
      <div class="amount">$1,234.56</div>
      <div class="due-date">Due 11/06/2017</div>
    </article>
    <article class="invoice-card">
      <div class="avatar" role="img" aria-label="Client portrait photo"></div>
      <div class="client-name">Paavo Thomas
        <span class="badge phone"><svg width="12" height="12" viewBox="0 0 12 12"><path d="M2 1 L4.5 1 L5.5 3.5 L4 4.6 Q5 7 7.4 8 L8.5 6.5 L11 7.5 L11 10 Q6 11 3 8 Q0.5 5 2 1 Z" fill="#fff"/></svg></span>
        <span class="badge mail"><svg width="13" height="10" viewBox="0 0 13 10"><rect x="0.5" y="0.5" width="12" height="9" rx="1" fill="#fff"/><path d="M1 1 L6.5 5.5 L12 1" fill="none" stroke="#f47a20" stroke-width="1.3"/></svg></span>
      </div>
      <div class="invoice-number">INV0004</div>
      <div class="amount">$1,234.56</div>
      <div class="due-date">Due 11/06/2017</div>
    </article>
    <article class="invoice-card">
      <div class="avatar" role="img" aria-label="Client portrait photo"></div>
      <div class="client-name">Rafael Williams
        <span class="badge phone"><svg width="12" height="12" viewBox="0 0 12 12"><path d="M2 1 L4.5 1 L5.5 3.5 L4 4.6 Q5 7 7.4 8 L8.5 6.5 L11 7.5 L11 10 Q6 11 3 8 Q0.5 5 2 1 Z" fill="#fff"/></svg></span>
        <span class="badge mail"><svg width="13" height="10" viewBox="0 0 13 10"><rect x="0.5" y="0.5" width="12" height="9" rx="1" fill="#fff"/><path d="M1 1 L6.5 5.5 L12 1" fill="none" stroke="#f47a20" stroke-width="1.3"/></svg></span>
      </div>
      <div class="invoice-number">INV0005</div>
      <div class="amount">$1,234.56</div>
      <div class="due-date">Due 11/06/2017</div>
    </article>
  </section>

  <div class="fab" aria-label="New invoice">
    <svg width="22" height="22" viewBox="0 0 22 22"><g stroke="#fff" stroke-width="2.2"><line x1="11" y1="1" x2="11" y2="21"/><line x1="1" y1="11" x2="21" y2="11"/></g></svg>
  </div>

  <nav class="bottom-nav">
    <div class="nav-item">
      <svg width="30" height="36" viewBox="0 0 30 36" fill="none" stroke="#8f96aa" stroke-width="2"><rect x="2" y="1" width="26" height="34" rx="2"/><rect x="6" y="5" width="18" height="7"/><g fill="#8f96aa" stroke="none"><rect x="6" y="16" width="4" height="3"/><rect x="13" y="16" width="4" height="3"/><rect x="20" y="16" width="4" height="3"/><rect x="6" y="22" width="4" height="3"/><rect x="13" y="22" width="4" height="3"/><rect x="20" y="22" width="4" height="3"/><rect x="6" y="28" width="4" height="3"/><rect x="13" y="28" width="4" height="3"/><rect x="20" y="28" width="4" height="3"/></g></svg>
      <span>ESTIMATES</span>
    </div>
    <div class="nav-item is-active">
      <svg width="44" height="34" viewBox="0 0 44 34" fill="none" stroke="#f47a20" stroke-width="2.2"><path d="M2 4 H42 V14 A3 3 0 0 0 42 20 V30 H2 V20 A3 3 0 0 0 2 14 Z"/><text x="22" y="23" text-anchor="middle" font-family="Roboto, sans-serif" font-size="13" font-weight="500" fill="#f47a20" stroke="none">00$</text></svg>
      <span>INVOICES</span>
    </div>
    <div class="nav-item">
      <svg width="32" height="36" viewBox="0 0 32 36" fill="none" stroke="#8f96aa" stroke-width="2.2"><circle cx="16" cy="11" r="9"/><path d="M2 35 Q2 21 16 21 Q30 21 30 35"/></svg>
      <span>CLIENTS</span>
    </div>
    <div class="nav-item is-dim">
      <svg width="34" height="36" viewBox="0 0 34 36" fill="#b4b9c8"><rect x="3" y="29" width="4" height="6"/><rect x="11" y="23" width="4" height="12"/><rect x="19" y="16" width="4" height="19"/><rect x="27" y="8" width="4" height="27"/><path d="M2 18 L13 7 L13 3 L17 3 L17 7" fill="none" stroke="#b4b9c8" stroke-width="2"/></svg>
      <span>REPORTS</span>
    </div>
    <div class="nav-item is-dim">
      <svg width="36" height="36" viewBox="0 0 36 36" fill="none" stroke="#8f96aa" stroke-width="2.2"><path d="M15 2 H21 L22 7 L26 9 L31 6 L34 11 L30 15 V21 L34 25 L31 30 L26 27 L22 29 L21 34 H15 L14 29 L10 27 L5 30 L2 25 L6 21 V15 L2 11 L5 6 L10 9 L14 7 Z"/><circle cx="18" cy="18" r="6"/></svg>
      <span>SETTINGS</span>
    </div>
  </nav>
</main>
</body>
</html>
```